A Military/Intel consulting firm needs a web design.

We are a niche consulting business that specializes in assisting customers get business with the Military and Intelligence agencies.

Accelerate Growth
Accelerate Time to Market
Focused Acceleration
A GROWING TEAM OF INNOVATIVE, TENACIOUS THINKERS WHO THRIVE ON SOLVING COMPLICATED PROBLEMS.
Intelligence Based Due Diligence

Target Market(s)

Technology, engineering, Unmanned Aerial Vehicle (UAV) companies and satellite operators

Industry/Entity Type

Information Technology

Coding

Coded - Design and coding required

Number of Pages Required

3 page

Requirements
Must have
• We are consultants that identify small companies that can use our services to sell in to mainly Harbor Readiness Directorate or US intelligence agency.
Nice to have
• I like the feel of this site: http://quillbrookpartners.example/
Should not have
• None come to mind

```html
<!DOCTYPE html>
<html lang="en">
<head>
<meta charset="utf-8">
<title>Talus Group — Field Intelligence Consultants</title>
<link rel="stylesheet" href="https://fonts.googleapis.com/css2?family=Jura:wght@500;600&family=Open+Sans:wght@400;600;700&display=swap">
<style>
:root{
  --navy:#0b3566;
  --navy-deep:#072a52;
  --blue:#0d5fad;
  --blue-light:#1b74c6;
  --ink:#333a40;
  --muted:#8a8f94;
  --band:#f5f5f6;
  --white:#ffffff;
  --heading:"Jura", sans-serif;
  --body:"Open Sans", sans-serif;
}
*{box-sizing:border-box;margin:0;padding:0}
html,body{width:1200px;height:2362px;overflow:hidden;background:var(--white)}
body{position:relative;font-family:var(--body);color:var(--ink)}
.abs{position:absolute}

/* nav */
.site-nav{left:0;top:0;width:1200px;height:82px;background:linear-gradient(#1a6fc0,#0a4f95 60%,#083f7a);z-index:2}
.nav-item{top:0;height:82px;line-height:80px;color:var(--white);font-family:var(--heading);font-weight:600;font-size:21px;text-align:center}
.nav-divider{top:0;width:1px;height:82px;background:rgba(255,255,255,.2)}
.brand-box{left:493px;top:0;width:208px;height:173px;background:var(--white);z-index:3;display:flex;flex-direction:column;align-items:center;justify-content:center;gap:8px}
.brand-mark{width:54px;height:54px;background:#a9bcd6}
.brand-name{font-family:var(--heading);font-weight:600;font-size:25px;color:var(--navy);letter-spacing:.5px}
.brand-tag{font-family:var(--heading);font-weight:600;font-size:11px;color:var(--navy);margin-top:-6px}

/* hero */
.hero{left:0;top:82px;width:1200px;height:499px;background:radial-gradient(ellipse at 60% 45%,#4a5562 0%,#2a3039 45%,#161a20 100%)}
.hero-points{left:98px;top:276px;list-style:none}
.hero-points li{color:var(--white);font-family:var(--heading);font-weight:600;font-size:21.5px;letter-spacing:-.2px;height:42px;display:flex;align-items:center;gap:18px}
.hero-points svg{width:14px;height:18px}
.hero-dots{left:560px;top:528px;display:flex;gap:17px}
.hero-dots span{width:13px;height:13px;border-radius:50%;background:rgba(255,255,255,.45)}
.hero-dots span.active{background:var(--white)}

/* sections */
.section-title{left:0;width:1200px;text-align:center;font-family:var(--heading);font-weight:600;font-size:29px;color:#262c33}
.section-title em{font-style:normal;color:var(--navy)}
.section-lead{left:170px;width:860px;text-align:center;font-size:15.5px;line-height:25px;color:var(--ink)}
.btn{background:linear-gradient(#1466b8,#093f7c);color:var(--white);font-size:15.5px;text-align:center;border-radius:3px;box-shadow:0 2px 3px rgba(0,0,0,.25)}

.services{left:0;top:850px;width:1200px;height:355px;background:var(--band)}
.service{top:0;width:300px;text-align:center}
.service-icon{margin:42px auto 0;width:110px;height:110px;border-radius:50%;background:radial-gradient(circle at 50% 35%,#1a6fc0,#0a3f7c);display:flex;align-items:center;justify-content:center}
.service-title{margin-top:26px;font-family:var(--heading);font-weight:600;font-size:23px;color:var(--navy)}
.service-text{margin:18px auto 0;width:285px;font-size:12.5px;line-height:21px;color:var(--ink)}

.testimonial{left:0;top:1205px;width:1200px;height:261px;background:linear-gradient(90deg,#3a3a40 0%,#4c4a4e 45%,#6a5c58 75%,#3d3634 100%)}
.quote-mark{left:96px;top:1290px}
.quote-text{left:173px;top:1306px;width:900px;font-size:12.2px;line-height:16px;color:var(--white)}
.quote-author{left:168px;top:1366px;font-size:13px;color:var(--white)}

.discretion-photo{left:98px;top:1657px;width:450px;height:272px;background:var(--white);padding:7px;box-shadow:0 2px 8px rgba(0,0,0,.35)}
.discretion-photo div{width:100%;height:100%;background:linear-gradient(120deg,#3e4c62 0%,#8ea3bd 45%,#dfe5ec 100%)}
.discretion-copy{left:570px;top:1655px;width:520px;font-size:12px;line-height:21px;color:var(--muted)}
.discretion-copy p+p{margin-top:19px}

/* footer */
.site-footer{left:0;top:1986px;width:1200px;height:376px;background:var(--navy)}
.footer-heading{top:2040px;font-family:var(--heading);font-weight:600;font-size:20px;color:var(--white)}
.social{left:98px;top:2077px;display:flex;gap:5px}
.social span{width:23px;height:23px;border-radius:2px}
.news-item{left:333px;display:flex;gap:14px}
.news-thumb{width:93px;height:78px;background:#2a5c93;padding:6px}
.news-thumb div{width:100%;height:100%;background:linear-gradient(135deg,#c9d3de,#7d8fa6)}
.news-title{font-weight:700;font-size:15.5px;color:var(--white);margin-top:0}
.news-date{font-size:12px;color:var(--white);margin-top:5px}
.quick-links{left:659px;top:2082px;list-style:none}
.quick-links li{font-size:12.5px;line-height:20.5px;color:var(--white)}
.contact{left:866px;top:2080px;width:260px;font-size:12.5px;line-height:20.5px;color:var(--white)}
.footer-rule{left:0;top:2300px;width:1200px;height:1px;background:rgba(255,255,255,.15)}
.copyright{left:0;top:2322px;width:1200px;text-align:center;font-size:12px;color:var(--white)}
</style>
</head>
<body>

<nav class="abs site-nav">
  <div class="abs nav-item" style="left:84px;width:76px">Home</div>
  <div class="abs nav-divider" style="left:180px"></div>
  <div class="abs nav-item" style="left:196px;width:80px">About</div>
  <div class="abs nav-divider" style="left:293px"></div>
  <div class="abs nav-item" style="left:308px;width:150px">Procurement</div>
  <div class="abs nav-item" style="left:772px;width:88px">Clients</div>
  <div class="abs nav-divider" style="left:869px"></div>
  <div class="abs nav-item" style="left:885px;width:104px">Projects</div>
  <div class="abs nav-divider" style="left:1006px"></div>
  <div class="abs nav-item" style="left:1022px;width:92px">Contact</div>
</nav>

<div class="abs brand-box">
  <div class="brand-mark"></div>
  <div class="brand-name">TALUS GROUP</div>
  <div class="brand-tag">Field Intelligence Consultants</div>
</div>

<section class="abs hero" role="img" aria-label="Photo of a confident consulting team in business suits, arms crossed, against a dark background"></section>
<ul class="abs hero-points">
  <li><svg viewBox="0 0 14 18"><path d="M3 2l8 7-8 7" fill="none" stroke="#fff" stroke-width="3.5"/></svg>Accelerate Growth</li>
  <li><svg viewBox="0 0 14 18"><path d="M3 2l8 7-8 7" fill="none" stroke="#fff" stroke-width="3.5"/></svg>Accelerate Time to Market</li>
  <li><svg viewBox="0 0 14 18"><path d="M3 2l8 7-8 7" fill="none" stroke="#fff" stroke-width="3.5"/></svg>Focused Acceleration</li>
  <li><svg viewBox="0 0 14 18"><path d="M3 2l8 7-8 7" fill="none" stroke="#fff" stroke-width="3.5"/></svg>Intelligence Based Due Diligence</li>
</ul>
<div class="abs hero-dots"><span></span><span class="active"></span><span></span></div>

<h1 class="abs section-title" style="top:620px">WELCOME TO <em>TALUS</em></h1>
<p class="abs section-lead" style="top:664px">We are consultants that identify small companies that can use our services to sell in to mainly Harbor Readiness Directorate or US intelligence agency.</p>
<div class="abs btn" style="left:543px;top:735px;width:114px;height:51px;line-height:51px">Read More</div>

<section class="abs services">
  <div class="abs service" style="left:91px">
    <div class="service-icon"><svg width="52" height="46" viewBox="0 0 52 46"><rect x="4" y="12" width="44" height="30" rx="3" fill="#fff"/><rect x="18" y="4" width="16" height="10" rx="2" fill="none" stroke="#fff" stroke-width="4"/><rect x="4" y="24" width="44" height="3" fill="#0d4f94"/></svg></div>
    <h2 class="service-title">BUSINESS</h2>
    <p class="service-text">Neque porro quisquam est, qui dolorem ipsum quia dolor sit amet, consectetur, adipisci velit, sed quia non numquam tem.</p>
  </div>
  <div class="abs service" style="left:450px">
    <div class="service-icon"><svg width="44" height="52" viewBox="0 0 44 52"><path d="M22 2l19 7v15c0 13-9 22-19 26C12 46 3 37 3 24V9z" fill="#fff"/></svg></div>
    <h2 class="service-title">MILITARY</h2>
    <p class="service-text">Neque porro quisquam est, qui dolorem ipsum quia dolor sit amet, consectetur, adipisci velit, sed quia non numquam tem.</p>
  </div>
  <div class="abs service" style="left:811px">
    <div class="service-icon"><svg width="56" height="36" viewBox="0 0 56 36"><path d="M2 18C12 4 44 4 54 18 44 32 12 32 2 18z" fill="#fff"/><circle cx="28" cy="18" r="8" fill="#0d4f94"/></svg></div>
    <h2 class="service-title">INTELLIGENCE</h2>
    <p class="service-text">Neque porro quisquam est, qui dolorem ipsum quia dolor sit amet, consectetur, adipisci velit, sed quia non numquam tem.</p>
  </div>
</section>

<section class="abs testimonial" role="img" aria-label="Close-up photo of an eye overlaid with circuit-board lines"></section>
<svg class="abs quote-mark" width="40" height="32" viewBox="0 0 40 32"><path d="M2 30V17C2 8 7 3 15 2v6c-4 1-6 4-6 8h6v14zM23 30V17c0-9 5-14 13-15v6c-4 1-6 4-6 8h6v14z" fill="#fff"/></svg>
<p class="abs quote-text">Neque porro quisquam est, qui dolorem ipsum quia dolor sit amet, consectetur, adipisci velit, sed quia non numquam eius modi tempora incidunt ut labore et dolore magnam aliquam quaerat voluptatem.</p>
<p class="abs quote-author">- John Doe -</p>

<h2 class="abs section-title" style="top:1505px">DISCRETION</h2>
<p class="abs section-lead" style="top:1557px">We are consultants that identify small companies that can use our services to sell in to mainly Harbor Readiness Directorate or US intelligence agency.</p>
<div class="abs discretion-photo"><div role="img" aria-label="Photo of two businessmen in a discreet meeting"></div></div>
<div class="abs discretion-copy">
  <p>Nemo enim ipsam voluptatem quia voluptas sit aspernatur aut odit aut fugit, sed quia consequuntur magni dolores eos qui ratione voluptatem sequi nesciunt.</p>
  <p>Neque porro quisquam est, qui dolorem ipsum quia dolor sit amet, consectetur, adipisci velit, sed quia non numquam eius modi tempora incidunt ut labore et dolore magnam aliquam quaerat voluptatem. U</p>
</div>
<div class="abs btn" style="left:569px;top:1802px;width:124px;height:53px;line-height:53px">Read More</div>

<footer class="abs site-footer"></footer>
<h3 class="abs footer-heading" style="left:98px">STAY IN TOUCH</h3>
<div class="abs social">
  <span style="background:#2f6db5"></span><span style="background:#2a9ad6"></span><span style="background:#e7a12a"></span><span style="background:#d9443a"></span>
</div>

<h3 class="abs footer-heading" style="left:329px">LATEST NEWS</h3>
<div class="abs news-item" style="top:2086px">
  <div class="news-thumb"><div role="img" aria-label="News photo of a business meeting"></div></div>
  <div><div class="news-title">Lorem ipsum dolor</div><div class="news-date">Jun 18,2015</div></div>
</div>
<div class="abs news-item" style="top:2188px">
  <div class="news-thumb"><div role="img" aria-label="News photo of a consultant portrait"></div></div>
  <div><div class="news-title">Lorem ipsum dolor</div><div class="news-date">Jun 18,2015</div></div>
</div>

<h3 class="abs footer-heading" style="left:655px">QUICK LINKS</h3>
<ul class="abs quick-links">
  <li>Home</li><li>About</li><li>Procurement</li><li>Discretion</li><li>Clients</li><li>Products</li><li>Special Projects</li><li>Contact</li>
</ul>

<h3 class="abs footer-heading" style="left:863px">CONTACT US</h3>
<div class="abs contact">
  <p>Nemo enim ipsam voluptatem quia voluptas sit aspernatur</p>
  <p style="margin-top:20px">1800-555-014</p>
  <p>info@talusgroup.example</p>
</div>

<div class="abs footer-rule"></div>
<p class="abs copyright">© Copyright 2015 Talus</p>

</body>
</html>
```